Business card - house cleaning company

We want friendly high end business card highlighting our services . NO LOGOs on back of card please.. no vertical cards NO DOUBLE BROOMS

2 owners of the company: Corinne Halvey & Joel Brandt

Included phone number: (555)318-2047

Email: brightlanetidy@mailnest.example

Website: www.brightlanetidy.example

Bonded & Insured

Estes Park, CO 80517

Slogan maybe: Bringing a brighter shine to every corner of home

We want elegant high end card for house cleaning service. Maybe 2 sided if needed. Can it have bullet points of some services we offer

Residential Home Cleaning
Vacation Rental Cleaning
Commercial Cleaning
Carpet Cleaning
Window Cleaning
Property Management
Property Inspections
Property Maintenance
Trash Removal
Concierge Services

Highlight service on back of card. If we can do a one sided card with all this that’s great as well. Not cartoony.

Our logo attached and a design somone I had Perrin but they put very little time in. Not Unique enough. If you can do a custom design with a feminine touch that be great.

You will be eliminated for not reading the brief. NO DOUBLE LOGOS NO DOUBLE BROOMS. PLEASE BE CREATIVE. IF POST SAME LOGO WITH SMAL CHANGES RHEY WILL BE ELIMINATED. BE CREATIVE.

Thank you everyone for your designs. please only use the logo 1 time. and would love to see some that dont look all the same. We appreciate your time.

Target Market(s)

Residential and vacation rental home cleaning maid service

Industry/Entity Type

House cleaning maid services

Contact Information for Business Card

For business card use logo. black and green one provided. others for example. I wil try find some example.. We want friendly high end look. 2 owners of the company: Corinne Halvey & Joel Brandt Included phone number: (555)318-2047 Email: brightlanetidy@mailnest.example Website: www.brightlanetidy.example Bonded & Insured Estes Park, CO Slogan maybe: Bringing a brighter shine to every corner of home or Quality Service Guaranteed We want elegant high end card for house cleaning service. Maybe 2 sided if needed. Can it have bullet points of some services we offer Residential Home Cleaning Vacation Rental Cleaning Commercial Cleaning Carpet Cleaning Window Cleaning Property Management Property Inspections Property Maintenance Trash Removal Concierge Services

Requirements
Must have
• For business card use logo . Creativity. black and green one provided. We want friendly high end look. 2 owners of the company: Corinne Halvey & Joel Brandt Included phone number: (555)318-2047 Email: brightlanetidy@mailnest.example Website: www.brightlanetidy.example Licensed Bonded & Insured Estes Park, CO Slogan maybe: Bringing a brighter shine to every corner of home or Quality Service Guaranteed We want elegant high end card for house cleaning service. Maybe 2 sided if needed. Can it have bullet points of some services we offer Residential Home Cleaning Vacation Rental Cleaning Commercial Cleaning Carpet Cleaning Window Cleaning Property Management Property Inspections Property Maintenance Trash Removal Concierge Services .. creatitivty a plus. whimsical. we like stars..
Nice to have
• we want much better than the example of biz card provided as example. logo has colors that are in our website palette as well. We are open to ideas for the business card design. Will pay tip to best work. PLEASE USE COMPLIMENTING COLORS. . WE LIKE BLACK AND WHITE, stars
Should not have
• NO DOUBLE LOGOS. READ READ. READ. YOU WILL BE ELIMINATED no double logos or double brooms same side of card. I want didfrent examples. please don't make all your submission look the same

```html
<!DOCTYPE html>
<html lang="en">
<head>
<meta charset="utf-8">
<title>Bright Lane Cleaning Services – Business Card</title>
<link href="https://fonts.googleapis.com/css2?family=Roboto:wght@400;500;700&display=swap" rel="stylesheet">
<style>
  :root {
    --page: #2a2a2a;
    --card: #161616;
    --blue: #2f6d9e;
    --green: #6f9d3c;
    --white: #f2f2f2;
  }
  * { margin: 0; padding: 0; box-sizing: border-box; }
  html, body { width: 1200px; height: 900px; overflow: hidden; }
  body {
    background: var(--page);
    font-family: "Roboto", Arial, sans-serif;
    color: var(--white);
    position: relative;
  }
  .card {
    position: absolute;
    left: 250px;
    width: 700px;
    height: 400px;
    background: var(--card);
    box-shadow: 0 10px 30px rgba(0,0,0,.45);
  }
  .card--front { top: 30px; }
  .card--back { top: 470px; }

  .brand {
    position: absolute;
    left: 40px; top: 110px;
    display: flex;
    align-items: center;
    gap: 12px;
  }
  .brand__dot {
    width: 14px; height: 14px;
    border-radius: 50%;
    background: var(--green);
    flex: none;
  }
  .brand__name {
    font-size: 38px;
    font-weight: 500;
    color: var(--blue);
    line-height: 1.05;
    width: 260px;
  }

  .slogan {
    position: absolute;
    left: 40px; top: 280px;
    width: 300px;
    color: var(--green);
    font-size: 17px;
    line-height: 1.4;
  }
  .divider {
    position: absolute;
    left: 360px; top: 60px;
    width: 1px; height: 280px;
    background: var(--blue);
  }
  .contact {
    position: absolute;
    left: 390px; top: 80px;
    width: 290px;
  }
  .contact__owners {
    color: var(--green);
    font-weight: 700;
    font-size: 19px;
    line-height: 1.3;
    margin-bottom: 10px;
  }
  .contact__license { font-size: 15px; margin-bottom: 14px; }
  .contact__list { list-style: none; }
  .contact__item {
    display: flex;
    align-items: center;
    gap: 10px;
    font-size: 14.5px;
    margin-bottom: 9px;
  }
  .contact__item svg { width: 15px; height: 15px; flex: none; fill: var(--green); }

  .services {
    position: absolute;
    left: 30px; right: 30px; top: 0; bottom: 0;
    display: flex;
    flex-direction: column;
    justify-content: center;
    text-align: center;
    font-size: 17px;
    line-height: 2;
  }
  .services .bullet { color: var(--green); margin: 0 7px; }
</style>
</head>
<body>

<section class="card card--front" aria-label="Card front">
  <div class="brand">
    <span class="brand__dot"></span>
    <span class="brand__name">Bright Lane Cleaning Services</span>
  </div>
  <p class="slogan">Bringing a brighter shine to every corner of home</p>
  <div class="divider"></div>
  <div class="contact">
    <p class="contact__owners">Corinne Halvey &amp; Joel Brandt</p>
    <p class="contact__license">Licensed Bonded &amp; Insured</p>
    <ul class="contact__list">
      <li class="contact__item">
        <svg viewBox="0 0 24 24"><path d="M6.6 10.8a15.1 15.1 0 0 0 6.6 6.6l2.2-2.2a1 1 0 0 1 1-.25 11.4 11.4 0 0 0 3.6.57 1 1 0 0 1 1 1V20a1 1 0 0 1-1 1A17 17 0 0 1 3 4a1 1 0 0 1 1-1h3.5a1 1 0 0 1 1 1c0 1.25.2 2.45.57 3.57a1 1 0 0 1-.25 1z"/></svg>
        (555) 318-2047
      </li>
      <li class="contact__item">
        <svg viewBox="0 0 24 24"><path d="M2 5h20v2l-10 6L2 7zm0 4.3 10 6 10-6V19H2z"/></svg>
        brightlanetidy@mailnest.example
      </li>
      <li class="contact__item">
        <svg viewBox="0 0 24 24"><circle cx="12" cy="12" r="10" fill="none" stroke="#6f9d3c" stroke-width="2"/><path d="M2 12h20M12 2c3 3 3 17 0 20M12 2c-3 3-3 17 0 20" fill="none" stroke="#6f9d3c" stroke-width="2"/></svg>
        www.brightlanetidy.example
      </li>
      <li class="contact__item">
        <svg viewBox="0 0 24 24"><path d="M12 2a7 7 0 0 0-7 7c0 5 7 13 7 13s7-8 7-13a7 7 0 0 0-7-7zm0 9.5A2.5 2.5 0 1 1 12 6.5a2.5 2.5 0 0 1 0 5z"/></svg>
        Estes Park, CO 80517
      </li>
    </ul>
  </div>
</section>

<section class="card card--back" aria-label="Card back">
  <div class="services">
    <p>Residential Home Cleaning<span class="bullet">•</span>Vacation Rental Cleaning<span class="bullet">•</span>Commercial Cleaning</p>
    <p>Carpet Cleaning<span class="bullet">•</span>Window Cleaning<span class="bullet">•</span>Property Management</p>
    <p>Property Inspections<span class="bullet">•</span>Property Maintenance<span class="bullet">•</span>Trash Removal</p>
    <p>Concierge Services</p>
  </div>
</section>

</body>
</html>
```